Design Product Packaging label for Bags with Superfood products in Photoshop

Design a product label for bags with superfood. (Label size 1/4 of A4 page (10cm x 14cm) Start with 1 product packaging for Maca Powder.

Main target:
Attractive packaging for European consumers who looking for healthy natural energetic food supplements.

The winner will get constant orders from me for all our products (20+), including promotion designs for Marketvale listings and website.

1. Size of the label 10cm x 14cm.
We will print it on the white sticky label and stick it to the brown paper Standy Pouch.
2. logo included (Logo was recently designed. If you believe it might be improved, feel free to edit it. We thought to redesign it, to make it looks good in the circle format for social media )
3. Text front and back side included in the word doc.
4. Our brand name is Vitalbrook. It is Organic healthy natural products. Natural health, natural energy. This order is for Maca Powder but later we want to apply the same design to all other products such as Cacao beans, hemp protein, berry, etc.
5. All information for the label you can find in the word file. Additional information such as nutritional information you can find in the PDF file.

The preferable format is photoshop PSD file.

```html
<!DOCTYPE html>
<html lang="en">
<head>
<meta charset="utf-8">
<title>Vitalbrook Organic Raw Maca Powder Label</title>
<link href="https://fonts.googleapis.com/css2?family=Montserrat:wght@500;600;700;800&family=Questrial&display=swap" rel="stylesheet">
<style>
  :root {
    --page-bg: #f2f2f0;
    --band-green: #a5d59b;
    --strip-green: #b9e1af;
    --label-white: #ffffff;
    --ink-navy: #1c3d5e;
    --brand-teal: #2ba6a8;
    --frame-teal: #2ea3a1;
    --badge-green: #4fae4a;
    --badge-light: #e6f4e2;
    --root-dark: #1f4a3c;
  }
  * { box-sizing: border-box; margin: 0; padding: 0; }
  html, body {
    width: 1200px; height: 2400px; overflow: hidden;
    background: var(--page-bg);
  }
  .label {
    position: absolute; left: 50px; top: 427px;
    width: 1100px; height: 1546px;
    border: 4px solid var(--frame-teal);
    background: var(--label-white);
    display: flex; flex-direction: column;
    font-family: "Questrial", sans-serif;
    color: var(--ink-navy);
  }
  .brand-band {
    height: 352px; background: var(--band-green);
    display: flex; align-items: center; justify-content: center;
  }
  .brand-seal {
    width: 266px; height: 266px; border-radius: 50%;
    background: var(--label-white); border: 4px solid var(--ink-navy);
    display: flex; align-items: center; justify-content: center;
  }
  .brand-name {
    font-family: "Questrial", sans-serif; font-size: 40px;
    color: var(--brand-teal);
  }
  .title-panel {
    height: 533px; position: relative; padding: 36px 0 0 48px;
  }
  .title-kicker { font-size: 70px; letter-spacing: 1px; line-height: 1; }
  .title-product {
    font-family: "Montserrat", sans-serif; font-weight: 800;
    font-size: 158px; letter-spacing: 24px; line-height: 1; margin-top: 14px;
  }
  .title-form { font-size: 150px; line-height: 0.95; margin-top: -4px; }
  .title-tagline {
    position: absolute; left: 48px; bottom: 22px;
    font-size: 68px; line-height: 1; white-space: nowrap;
  }
  .root-illustration {
    position: absolute; left: 705px; top: 20px; width: 350px; height: 390px;
    border-radius: 45% 45% 50% 50%;
    background: radial-gradient(circle at 50% 65%, var(--brand-teal) 0%, #3a8f84 45%, var(--root-dark) 100%);
  }
  .badge-strip {
    height: 146px; background: var(--strip-green);
    display: flex; align-items: center; justify-content: space-around;
    padding: 0 30px;
  }
  .badge { width: 128px; height: 128px; display: block; }
  .benefits {
    height: 240px; display: flex; flex-direction: column;
    justify-content: center; align-items: center;
    font-family: "Montserrat", sans-serif; font-weight: 600;
    font-size: 43px; line-height: 1.5;
  }
  .origin-band {
    flex: 1; background: var(--band-green);
    display: flex; flex-direction: column; align-items: center;
    padding-top: 60px;
    font-family: "Montserrat", sans-serif;
  }
  .origin-line { display: flex; align-items: center; gap: 18px; }
  .origin-map {
    width: 44px; height: 80px;
    background: var(--brand-teal);
    border-radius: 40% 60% 45% 55%;
  }
  .origin-text { font-size: 42px; font-weight: 600; }
  .net-weight { font-size: 40px; font-weight: 700; margin-top: 40px; }
</style>
</head>
<body>
  <main class="label">
    <header class="brand-band">
      <div class="brand-seal"><span class="brand-name">Vitalbrook</span></div>
    </header>
    <section class="title-panel">
      <p class="title-kicker">ORGANIC RAW</p>
      <h1 class="title-product">MACA</h1>
      <p class="title-form">powder</p>
      <div class="root-illustration" role="img" aria-label="Illustration of a maca root with leafy top"></div>
      <p class="title-tagline">nutrient-rich superfoods</p>
    </section>
    <section class="badge-strip" aria-label="Certifications">
      <svg class="badge" viewBox="0 0 128 128" aria-hidden="true"><circle cx="64" cy="64" r="62" fill="#fff"/><circle cx="64" cy="64" r="54" fill="none" stroke="var(--badge-green)" stroke-width="6"/><circle cx="64" cy="64" r="38" fill="var(--badge-green)"/><path d="M46 65 L59 78 L83 52" fill="none" stroke="#fff" stroke-width="9" stroke-linecap="round" stroke-linejoin="round"/></svg>
      <svg class="badge" viewBox="0 0 128 128" aria-hidden="true"><circle cx="64" cy="64" r="62" fill="#fff"/><circle cx="64" cy="64" r="54" fill="none" stroke="var(--badge-green)" stroke-width="6"/><circle cx="64" cy="64" r="38" fill="var(--badge-light)"/><path d="M46 65 L59 78 L83 52" fill="none" stroke="var(--badge-green)" stroke-width="9" stroke-linecap="round" stroke-linejoin="round"/></svg>
      <svg class="badge" viewBox="0 0 128 128" aria-hidden="true"><circle cx="64" cy="64" r="62" fill="var(--badge-green)"/><circle cx="64" cy="64" r="50" fill="none" stroke="#fff" stroke-width="4"/><path d="M46 65 L59 78 L83 52" fill="none" stroke="#fff" stroke-width="9" stroke-linecap="round" stroke-linejoin="round"/></svg>
      <svg class="badge" viewBox="0 0 128 128" aria-hidden="true"><circle cx="64" cy="64" r="62" fill="var(--badge-green)"/><circle cx="64" cy="64" r="40" fill="#fff"/><path d="M46 65 L59 78 L83 52" fill="none" stroke="var(--badge-green)" stroke-width="9" stroke-linecap="round" stroke-linejoin="round"/></svg>
      <svg class="badge" viewBox="0 0 128 128" aria-hidden="true"><circle cx="64" cy="64" r="62" fill="#fff"/><circle cx="64" cy="64" r="54" fill="none" stroke="var(--badge-green)" stroke-width="6"/><path d="M46 65 L59 78 L83 52" fill="none" stroke="var(--badge-green)" stroke-width="9" stroke-linecap="round" stroke-linejoin="round"/></svg>
      <svg class="badge" viewBox="0 0 128 128" aria-hidden="true"><circle cx="64" cy="50" r="36" fill="var(--badge-green)"/><path d="M48 51 L59 62 L80 40" fill="none" stroke="#fff" stroke-width="8" stroke-linecap="round" stroke-linejoin="round"/><rect x="34" y="98" width="60" height="8" rx="4" fill="var(--badge-green)"/><rect x="42" y="112" width="44" height="8" rx="4" fill="var(--badge-green)"/></svg>
    </section>
    <section class="benefits">
      <p>*Boost Energy *Antioxidant *Immune Booster</p>
      <p>*Improve Mood *Healthy Skin</p>
      <p>*Anti-aging *Balance Hormones</p>
    </section>
    <footer class="origin-band">
      <div class="origin-line">
        <div class="origin-map" role="img" aria-label="Map outline of Peru"></div>
        <p class="origin-text">Product of Peru</p>
      </div>
      <p class="net-weight">Weight: 220g</p>
    </footer>
  </main>
</body>
</html>
```